We would like to incorporate our logo into letterhead design and envelopes. We are looking for something that is moderately conservative but not old law firm style. Both the envelopes and the letterhead must have both firm addresses. We would like to incorporate the color of the logo, but only a small amount of color - perhaps on one of the borders. The addresses for the firm locations are listed below. Given that it is a law firm, it needs to somewhat conservative, but not the old school, small black font on cream colored paper design.

The firm addresses are:

27815 N. Harlow Pemberton Pkwy.
Ste 4200
Scottsdale, AZ 85391

6100 W. Cedar Avenue
Ste 700
Burbank, CA 91623

Industry/Entity Type

Legal

Colors

Designer to choose colors to be used in the design.

Requirements
Must have
• Both addresses:
• 27815 N. Harlow Pemberton Pkwy.
• Ste 4200
• Scottsdale, AZ 85391
• 6100 W. Cedar Avenue
• Ste 700
• Burbank, CA 91623
Nice to have
• Small amount of color on border(s) that matches the logo but not too much color

```html
<!DOCTYPE html>
<html lang="en">
<head>
<meta charset="utf-8">
<title>Halvern Law — Letterhead &amp; Envelopes</title>
<link rel="stylesheet" href="https://fonts.googleapis.com/css2?family=Marcellus&family=Open+Sans:wght@400&display=swap">
<style>
  :root {
    --backdrop: #c4c4c4;
    --paper: #f8f2e3;
    --paper-shade: #f3ecdc;
    --navy: #2b2858;
    --ink: #3a3a48;
    --flap-line: #e6dcc6;
  }
  * { margin: 0; padding: 0; box-sizing: border-box; }
  html, body {
    width: 1200px; height: 1199px; overflow: hidden;
    background: var(--backdrop);
  }
  .stage { position: relative; width: 1200px; height: 1199px; }

  .sheet {
    position: absolute;
    background: var(--paper);
  }
  .sheet--edge::before {
    content: ""; position: absolute; left: 0; top: 0; bottom: 0;
    width: 9px; background: var(--navy);
  }

  .firm-name {
    font-family: "Marcellus", serif;
    font-weight: 400;
    color: var(--navy);
    letter-spacing: 0.02em;
    white-space: nowrap;
    line-height: 1;
  }
  .addresses {
    font-family: "Open Sans", sans-serif;
    font-size: 5.4px;
    color: var(--ink);
    white-space: nowrap;
    line-height: 1;
  }

  /* Letterhead */
  .letterhead { left: 135px; top: 288px; width: 452px; height: 639px; }
  .letterhead .firm-name {
    position: absolute; top: 32px; left: 9px; right: 0;
    text-align: center; font-size: 20px;
  }
  .letterhead .addresses {
    position: absolute; bottom: 18px; left: 9px; right: 0;
    text-align: center;
  }

  /* Envelope back */
  .envelope-back { left: 638px; top: 451px; width: 456px; height: 227px; }
  .envelope-back svg { position: absolute; inset: 0; }

  /* Envelope front */
  .envelope-front { left: 638px; top: 702px; width: 456px; height: 227px; }
  .envelope-front .firm-name {
    position: absolute; left: 21px; bottom: 17px; font-size: 15px;
  }
  .envelope-front .addresses {
    position: absolute; left: 21px; bottom: 8px;
  }
</style>
</head>
<body>
<main class="stage">
  <section class="sheet sheet--edge letterhead" aria-label="Letterhead">
    <p class="firm-name">HALVERN LAW</p>
    <p class="addresses">27815 N. Harlow Pemberton Pkwy. Ste 4200, Scottsdale, AZ 85391 &nbsp;|&nbsp; 6100 W. Cedar Avenue Ste 700, Burbank, CA 91623</p>
  </section>

  <section class="sheet envelope-back" aria-label="Envelope back">
    <svg width="456" height="227" viewBox="0 0 456 227" aria-hidden="true">
      <path d="M1 1 L10 30 Q16 38 26 41 L200 96 Q226 104 252 97 L440 34 Q448 31 451 22 L455 1 Z"
            fill="var(--paper-shade)"/>
      <path d="M1 1 L10 30 Q16 38 26 41 L200 96 Q226 104 252 97 L440 34 Q448 31 451 22 L455 1"
            fill="none" stroke="var(--flap-line)" stroke-width="1"/>
    </svg>
  </section>

  <section class="sheet sheet--edge envelope-front" aria-label="Envelope front">
    <p class="firm-name">HALVERN LAW</p>
    <p class="addresses">27815 N. Harlow Pemberton Pkwy. Ste 4200, Scottsdale, AZ 85391 &nbsp;|&nbsp; 6100 W. Cedar Avenue Ste 700, Burbank, CA 91623</p>
  </section>
</main>
</body>
</html>
```